Website Home Page for Women's Health Medical Office

Redesign existing homepage for website using existing logo. Current website location is www.lumawomenscare.com. Please give it a modern, streamlined, playful feel.

Please give it a feminine feel and make it bright and cheerful using logo colors.

Target Market(s)

Women between the ages of 25-45

Industry/Entity Type

Medical Office

Coding

Coded - Design and coding required

Number of Pages Required

1 page

Font styles to use
Sans Serif
Other font styles liked:
• SEGOI UI script for text and GIL SANS for bold (or their equivilent)

Colors
E54698
E96AAD
F1A4CE
F9D9EA
FCEFF6

Requirements
Must have
• Existing logo. Logo Colors. Feminine, cheerful, simple design. all relevant contact information
Nice to have
• clean lines and streamlined look
Should not have
• Cluttered

```html
<!DOCTYPE html>
<html lang="en">
<head>
<meta charset="utf-8">
<title>Luma Women's Care — Home</title>
<link href="https://fonts.googleapis.com/css2?family=Montserrat:wght@500;700;800&family=Gilda+Display&family=Lato:wght@400;700&display=swap" rel="stylesheet">
<style>
:root{
  --pink:#E54698;
  --pink-mid:#E96AAD;
  --pink-soft:#F1A4CE;
  --pink-pale:#F9D9EA;
  --pink-mist:#FCEFF6;
  --ink:#161616;
  --text:#3a3a3a;
  --white:#ffffff;
  --black:#0b0b0b;
}
*{margin:0;padding:0;box-sizing:border-box}
html,body{width:1200px;height:5249px;overflow:hidden}
body{position:relative;background:var(--white);font-family:'Lato',sans-serif;color:var(--text)}
.abs{position:absolute}
.script{font-family:'Gilda Display',serif;color:var(--pink);font-weight:400}
.caps{font-family:'Montserrat',sans-serif;font-weight:800;color:var(--ink);text-transform:uppercase}
.btn{position:absolute;display:flex;align-items:center;justify-content:center;border-radius:22px;font-family:'Montserrat',sans-serif;font-size:11px;text-transform:uppercase;letter-spacing:.5px;color:var(--white);background:var(--pink)}
.btn b{font-weight:800;margin-left:4px}
.photo{position:absolute}

/* header */
.topbar{left:520px;top:0;width:680px;height:35px;background:var(--pink)}
.topbar .addr{position:absolute;left:30px;top:10px;color:#fff;font-size:11px;display:flex;gap:6px;align-items:center}
.topbar .mail{position:absolute;left:376px;top:0;width:194px;height:35px;background:#d63a89;color:#fff;font-size:11px;display:flex;align-items:center;justify-content:center;gap:6px}
.logo-box{left:112px;top:0;width:179px;height:157px;background:#fff;border:2px solid var(--pink-soft);display:flex;align-items:center;justify-content:center;gap:8px;z-index:3}
.logo-box span{font-family:'Montserrat',sans-serif;font-weight:800;font-size:15px;color:var(--pink);text-align:center;line-height:1.2}
.logo-dot{width:12px;height:12px;border-radius:50%;background:var(--pink)}
.nav{left:326px;top:66px;display:flex;gap:26px;font-family:'Montserrat',sans-serif;font-size:11px;font-weight:500;color:#222;text-transform:uppercase}
.nav .on{color:var(--pink);border-bottom:1px solid var(--pink);padding-bottom:4px}
.callus{left:727px;top:55px;display:flex;align-items:center;gap:8px}
.callus small{display:block;font-size:10px;color:#666}
.callus strong{font-family:'Montserrat',sans-serif;font-size:15px;color:var(--ink)}
.btn-outline{left:896px;top:56px;width:194px;height:36px;background:#fff;color:#222;border:2px solid var(--pink-soft)}

/* hero */
.hero{left:0;top:102px;width:1200px;height:600px;background:linear-gradient(90deg,#fdf7fa 0%,#fbeef4 35%,#f3f1f0 100%)}
.hero-photo{left:440px;top:102px;width:760px;height:520px;background:linear-gradient(110deg,rgba(253,247,250,0) 0%,#ece6e3 30%,#d9d2cf 60%,#f4f2f1 100%)}
.hero-tag{left:112px;top:252px;font-size:32px}
.hero-title{left:112px;top:298px;font-size:44px;line-height:43px;letter-spacing:1px}
.hero-rule{left:304px;top:404px;width:145px;height:2px;background:var(--pink)}
.hero-btn{left:110px;top:451px;width:211px;height:40px}

/* about */
.about-frame{left:110px;top:776px;width:368px;height:462px;border:2px solid var(--pink-soft)}
.about-photo1{left:124px;top:790px;width:512px;height:483px;background:linear-gradient(120deg,#6d5a4c,#a99a8c 45%,#d8d1cb 70%,#5a504a)}
.about-card{left:179px;top:1175px;width:410px;height:296px;background:#fff;border:2px solid var(--pink-soft);outline:12px solid #fff;text-align:center;padding:56px 34px 0}
.about-card p{font-size:13.5px;line-height:24px;color:#333}
.about-card .btn{left:124px;top:224px;width:160px;height:38px}
.about-head{left:640px;top:810px;width:480px;text-align:center}
.about-head .script{font-size:28px}
.about-head .caps{font-size:29px;line-height:31px;margin-top:6px}
.about-text{left:674px;top:940px;width:412px;text-align:center;font-size:10.5px;line-height:18px;color:#333}
.about-photo2{left:676px;top:1112px;width:378px;height:412px;background:linear-gradient(90deg,#d8d3cd,#b9a79a 40%,#e6e2dd 60%,#4c4442)}

/* band */
.band{left:0;top:1607px;width:1200px;height:367px;background:linear-gradient(90deg,#e0418f,#e54698 50%,#e7579f);text-align:center;color:#fff}
.band .tag{font-family:'Gilda Display',serif;font-size:32px;margin-top:72px}
.band .title{font-family:'Montserrat',sans-serif;font-weight:800;font-size:45px;line-height:47px;letter-spacing:1px;margin-top:6px}
.band .sub{font-size:14px;margin-top:14px;color:#fbe1ee}
.band .call{position:absolute;left:477px;top:253px;width:246px;height:44px;border:2px solid #fff;border-radius:24px;display:flex;align-items:center;justify-content:center;font-family:'Montserrat',sans-serif;font-size:13px}

/* services */
.services{left:0;top:1974px;width:1200px;height:751px;background:linear-gradient(180deg,#fff 0%,#fbf4f1 60%,#fdf3f4 100%)}
.services-head{left:0;top:2056px;width:1200px;text-align:center}
.services-head .script{font-size:31px}
.services-head .caps{font-size:29px;margin-top:4px;letter-spacing:1px}
.card{position:absolute;top:2173px;width:234px;height:406px;background:#fff;text-align:center;box-shadow:0 6px 18px rgba(0,0,0,.05)}
.card .pic{height:232px}
.card .icon{position:absolute;left:87px;top:202px;width:60px;height:60px;border-radius:50%;background:var(--pink-pale);border:4px solid #fff;display:flex;align-items:center;justify-content:center}
.card.active .icon{background:var(--pink)}
.card h3{margin-top:50px;font-family:'Montserrat',sans-serif;font-size:13px;font-weight:500;color:#222;text-transform:uppercase}
.card h3 b{font-weight:800}
.card p{margin:20px 18px 0;font-size:10.5px;line-height:16px;color:#555}
.card.active{height:456px;border-bottom:4px solid var(--pink)}
.card .more{position:absolute;left:51px;top:400px;width:132px;height:34px;border:2px solid var(--pink-soft);border-radius:20px;font-family:'Montserrat',sans-serif;font-size:10px;font-weight:800;display:flex;align-items:center;justify-content:center;color:#222}

/* mission */
.mission-icon{left:560px;top:2775px}
.mission-frame{left:210px;top:2864px;width:778px;height:318px;border:2px solid var(--pink-soft);border-bottom:none}
.mission-head{left:270px;top:2843px;width:660px;text-align:center;background:#fff}
.mission-head .script{font-size:29px}
.mission-head .caps{font-size:28px;line-height:31px;margin-top:6px}
.mission-text{left:300px;top:2994px;width:600px;text-align:center;font-size:13px;line-height:22px;color:#333}
.mission-text p+p{margin-top:12px}
.motto{left:0;top:3205px;width:1200px;text-align:center}
.motto small{font-family:'Montserrat',sans-serif;font-weight:700;font-size:13px;color:#222}
.motto .script{display:block;font-size:24px;margin-top:2px}
.sea{left:0;top:3262px;width:1200px;height:420px;background:linear-gradient(180deg,#fff 0%,#e9eef3 25%,#bfcbd6 60%,#9aa3ab 100%)}

/* team */
.team-photo{left:110px;top:3783px;width:352px;height:580px;background:radial-gradient(circle at 50% 35%,#4d6173,#24303b 70%,#17212a)}
.team-head{left:611px;top:3820px}
.team-head .script{font-size:31px}
.team-head .caps{font-size:27px;margin-top:6px;letter-spacing:.5px}
.team-box{left:521px;top:3921px;width:569px;height:491px;background:var(--pink-mist);border:1px solid var(--pink-pale);padding:44px 70px 0 96px;font-size:11.5px;line-height:15px;color:#333}
.team-box p+p{margin-top:14px}
.team-box a{color:#222;font-weight:700;text-decoration:underline}
.team-box .btn{left:96px;top:400px;width:212px;height:42px}

/* insurance */
.insure{left:0;top:4494px;width:1200px;height:513px;background:linear-gradient(90deg,#e0418f,#e54698 60%,#e85aa2)}
.notch{left:570px;top:4494px}
.plans{left:110px;top:4594px;width:980px;display:flex;flex-direction:column;gap:11px}
.plan-row{display:flex;gap:10px;justify-content:center}
.plan{height:42px;background:#fff;border:1px solid #f6c7de;display:flex;align-items:center;justify-content:center;gap:8px;padding:0 14px;font-family:'Montserrat',sans-serif;font-size:10px;font-weight:700;color:#222;text-transform:uppercase;flex-grow:1;white-space:nowrap}
.plan-row.last .plan{flex-grow:0;padding:0 22px}
.tick{flex:none}

/* footer */
.footer{left:0;top:5007px;width:1200px;height:242px;background:var(--black);color:#fff}
.foot-logo{left:509px;top:4909px;width:180px;height:180px;background:#fff;border:2px solid var(--pink-soft);display:flex;align-items:center;justify-content:center;gap:8px;z-index:3}
.foot-logo span{font-family:'Montserrat',sans-serif;font-weight:800;font-size:15px;color:var(--pink)}
.foot-addr{left:110px;top:5045px;font-size:12px;display:flex;gap:8px;align-items:center;color:#fff}
.foot-contact{right:110px;top:5045px;font-size:12px;display:flex;gap:10px;align-items:center;color:#fff}
.foot-nav{left:0;top:5112px;width:1200px;display:flex;justify-content:center;gap:24px;font-family:'Montserrat',sans-serif;font-size:11px;text-transform:uppercase;color:#fff}
.foot-copy{left:0;top:5158px;width:1200px;text-align:center;font-size:10px;color:#bbb;line-height:16px}
.foot-social{left:0;top:5200px;width:1200px;display:flex;justify-content:center;gap:14px}
.foot-social i{width:12px;height:12px;border-radius:50%;background:#fff;display:block}
</style>
</head>
<body>

<!-- header -->
<div class="abs topbar">
  <div class="addr"><svg width="12" height="16" viewBox="0 0 12 16"><path d="M6 0a6 6 0 0 0-6 6c0 4.5 6 10 6 10s6-5.5 6-10a6 6 0 0 0-6-6zm0 8.5A2.5 2.5 0 1 1 6 3.5a2.5 2.5 0 0 1 0 5z" fill="#fff"/></svg>1840 Willow Crest Drive, Suite 120, Lakeview, CA 92500</div>
  <div class="mail"><svg width="14" height="12" viewBox="0 0 14 12"><path d="M0 5 14 0 10 12 7 7z" fill="#fff"/></svg>admin@lumawomenscare.com</div>
</div>
<div class="abs logo-box"><i class="logo-dot"></i><span>Luma<br>Women's Care</span></div>
<nav class="abs nav"><span class="on">Home</span><span>About Us</span><span>Services</span><span>Resources</span><span>Contact</span></nav>
<div class="abs callus">
  <svg width="30" height="30" viewBox="0 0 24 24"><path d="M6.6 10.8a15 15 0 0 0 6.6 6.6l2.2-2.2c.3-.3.7-.4 1-.2 1.1.4 2.3.6 3.6.6.6 0 1 .4 1 1V20c0 .6-.4 1-1 1A17 17 0 0 1 3 4c0-.6.4-1 1-1h3.5c.6 0 1 .4 1 1 0 1.3.2 2.5.6 3.6.1.3 0 .7-.2 1z" fill="none" stroke="#222" stroke-width="1.6"/></svg>
  <div><small>Call Us Today!</small><strong>555- 610- 2480</strong></div>
</div>
<div class="btn btn-outline">Online <b>Appointment</b></div>

<!-- hero -->
<section class="abs hero"></section>
<div class="photo hero-photo" role="img" aria-label="Doctor in a white coat consulting with a pregnant patient at a desk"></div>
<div class="abs script hero-tag">Better Health Start Here!</div>
<h1 class="abs caps hero-title">Perrsonalized<br>Medical Care For<br>Women</h1>
<div class="abs hero-rule"></div>
<div class="btn hero-btn">Online <b>Appointment</b></div>
<svg class="abs" style="left:0;top:580px" width="1200" height="130" viewBox="0 0 1200 130">
  <path d="M270 42 C520 120 860 118 1200 22 L1200 40 C860 138 520 126 270 42 Z" fill="#E54698"/>
  <path d="M0 70 C300 140 800 140 1200 48 L1200 130 L0 130 Z" fill="#ffffff"/>
</svg>

<!-- about -->
<div class="abs about-frame"></div>
<div class="photo about-photo1" role="img" aria-label="Two smiling medical staff members in scrubs in a clinic hallway"></div>
<div class="abs about-card">
  <p>Our medical providers will take time to give you the personalized health care you deserve. This includes taking time to listen to you and screening you for problems to help ensure that any health issues are diagnosed and treated as early as possible.</p>
  <div class="btn">Know <b>More</b></div>
</div>
<div class="abs about-head">
  <div class="script">About Luma Women's Care,</div>
  <h2 class="caps">Serving Willow Springs<br>Medical Center</h2>
</div>
<p class="abs about-text">At Luma Women's Care in Lakeview, California, we believe better health starts when the patient is educated. For this reason, we take time to listen to our patients concerns, explain each option available, and to answer any questions our patients may have so that they can make informed decisions. At Luma Women's Care, our providers tailor every procedure performed and treatment option recommended to meet the specific needs of our patients. We remain up-to-date on the latest technology and practice guidelines for women's health.</p>
<div class="photo about-photo2" role="img" aria-label="Two women with a baby standing together outdoors"></div>

<!-- patients band -->
<section class="abs band">
  <div class="tag">Better Health Start Here!</div>
  <h2 class="title">NOW ACCEPTING<br>NEW PATIENTS</h2>
  <div class="sub">Click Here For An Appointment</div>
  <div class="call">CALL:- <b style="margin-left:4px">(555) 610-2480</b></div>
</section>

<!-- services -->
<section class="abs services"></section>
<div class="abs services-head">
  <div class="script">Health Services Offered</div>
  <h2 class="caps">How Can We Help You?</h2>
</div>
<article class="card" style="left:110px">
  <div class="pic" role="img" aria-label="Nurse examining a pregnant patient" style="background:linear-gradient(135deg,#3d4f73,#c89b88 55%,#e9dcd3)"></div>
  <div class="icon"><svg width="26" height="26" viewBox="0 0 24 24"><circle cx="12" cy="12" r="8" fill="none" stroke="#E54698" stroke-width="1.6"/><circle cx="12" cy="12" r="3" fill="#E54698"/></svg></div>
  <h3><b>Pregnancy</b> Care</h3>
  <p>Receiving regular care in pregnancy is important for the health of both you and your baby.</p>
</article>
<article class="card active" style="left:359px">
  <div class="pic" role="img" aria-label="Young woman taking a birth control pill" style="background:linear-gradient(135deg,#ece7e3,#d3bfb0 50%,#f4f1ee)"></div>
  <div class="icon"><svg width="26" height="26" viewBox="0 0 24 24"><circle cx="12" cy="12" r="8" fill="none" stroke="#fff" stroke-width="1.6"/><path d="M7 17 17 7" stroke="#fff" stroke-width="1.6"/></svg></div>
  <h3><b>Birth</b> Control</h3>
  <p>Our gynecologists are knowledgeable on all forms of birth control including the IUD, the implant, vaginal ring/insertion, birth control pills, and more!</p>
  <div class="more">KNOW MORE</div>
</article>
<article class="card" style="left:607px">
  <div class="pic" role="img" aria-label="Doctor performing a physical exam on a patient" style="background:linear-gradient(135deg,#8a6d5c,#d9c6b6 50%,#efe9e4)"></div>
  <div class="icon"><svg width="26" height="26" viewBox="0 0 24 24"><rect x="5" y="4" width="14" height="16" rx="2" fill="none" stroke="#E54698" stroke-width="1.6"/><path d="M9 10h6M12 7v6" stroke="#E54698" stroke-width="1.6"/></svg></div>
  <h3><b>Well Woman</b> Exams</h3>
  <p>Our providers will help you to stay healthy by performing a physical exam on you annually.</p>
</article>
<article class="card" style="left:856px">
  <div class="pic" role="img" aria-label="Pregnant woman sitting in a yoga pose at home" style="background:linear-gradient(135deg,#d9d1c8,#b9aa9b 50%,#efe8e1)"></div>
  <div class="icon"><svg width="26" height="26" viewBox="0 0 24 24"><circle cx="12" cy="8" r="3" fill="none" stroke="#E54698" stroke-width="1.6"/><path d="M7 20c0-5 2-8 5-8s5 3 5 8" fill="none" stroke="#E54698" stroke-width="1.6"/></svg></div>
  <h3><b>Women's</b> Health</h3>
  <p>Whether you are dealing with painful or irregular periods, fibroids, or other women's health issues, we can help.</p>
</article>

<!-- mission -->
<svg class="abs mission-icon" width="80" height="62" viewBox="0 0 80 62">
  <circle cx="42" cy="24" r="22" fill="#F9D9EA"/>
  <path d="M14 58 34 24 44 40 50 32 66 58 Z" fill="none" stroke="#E54698" stroke-width="2.5" stroke-linejoin="round"/>
  <path d="M34 24V6h12l-3 4 3 4H34" fill="none" stroke="#E54698" stroke-width="2"/>
</svg>
<div class="abs mission-frame"></div>
<div class="abs mission-head">
  <div class="script">Mission statement</div>
  <h2 class="caps">To Provide Christ-Centered, Whole<br>Patient Medical Care For Women</h2>
</div>
<div class="abs mission-text">
  <p>We Strive To Be The Premier Medical Office In The Valley Region By Keeping Our Patients Informed Of All Findings And Concerns, Educating Them On Their Treatment Options, And By Supporting Them Through All Their Life Events.</p>
  <p>We will exhibit the highest level of professionalism in our conduct, appearance and mannerisms. Most importantly, we exercise extreme patience, kindness, diligence and honesty with our patients and with each other.</p>
</div>
<div class="abs motto"><small>AT LUMA WOMEN'S CARE</small><span class="script">“Better Health Starts Here.”</span></div>
<div class="photo sea" role="img" aria-label="Woman in a sun hat raising her arms toward the sea at sunrise"></div>
<svg class="abs" style="left:0;top:3540px" width="1200" height="150" viewBox="0 0 1200 150">
  <path d="M0 40 C200 130 600 150 1200 60 L1200 150 L0 150 Z" fill="#fff"/>
  <path d="M0 30 C220 120 620 140 1200 50 L1200 68 C620 150 220 132 0 40 Z" fill="#E54698"/>
</svg>

<!-- team -->
<div class="photo team-photo" role="img" aria-label="Portrait of a smiling OB/GYN specialist with long hair"></div>
<div class="abs team-head">
  <div class="script">Meet The Team</div>
  <h2 class="caps">Your OB/GYN Specialists</h2>
</div>
<div class="abs team-box">
  <p>Luma Women's Care offers you the best care possible in a personalized setting. We are currently accepting patients. <a>Call our office now to make an appointment.</a></p>
  <p>Luma Women's Care (located near Willow Springs Hospital in Lakeview, CA) is a medical office that specializes in Christ-centered healthcare for women of all ages. Our team of exclusively female providers have years of experience taking care of women with a variety of pregnancy and gynecology concerns.</p>
  <p>Whether you need a routine examination, help during your pregnancy, have questions on birth control, or another female concern, we offer the best care possible for our patients. That is why better health starts here.</p>
  <p>Our office provides you with an environment where you can feel comfortable and where you know you will be in good hands. Our providers are leaders women's health. Dr. Harlow is a board certified obstetrician and gynecologist. Dr. Amari is a board eligible obstetrician and gynecologist.</p>
  <div class="btn">Online <b>Appointment</b></div>
</div>

<!-- insurance -->
<section class="abs insure"></section>
<svg class="abs notch" width="60" height="32" viewBox="0 0 60 32"><path d="M0 0H60L30 32Z" fill="#fff"/></svg>
<div class="abs plans">
  <div class="plan-row">
    <div class="plan"><svg class="tick" width="16" height="14" viewBox="0 0 16 14"><path d="M1 7 6 12 15 1" fill="none" stroke="#E54698" stroke-width="2.5"/></svg>Brightpath</div>
    <div class="plan"><svg class="tick" width="16" height="14" viewBox="0 0 16 14"><path d="M1 7 6 12 15 1" fill="none" stroke="#E54698" stroke-width="2.5"/></svg>Harbor Direct</div>
    <div class="plan"><svg class="tick" width="16" height="14" viewBox="0 0 16 14"><path d="M1 7 6 12 15 1" fill="none" stroke="#E54698" stroke-width="2.5"/></svg>Primeway of Lakeview</div>
    <div class="plan"><svg class="tick" width="16" height="14" viewBox="0 0 16 14"><path d="M1 7 6 12 15 1" fill="none" stroke="#E54698" stroke-width="2.5"/></svg>Sunvia</div>
    <div class="plan"><svg class="tick" width="16" height="14" viewBox="0 0 16 14"><path d="M1 7 6 12 15 1" fill="none" stroke="#E54698" stroke-width="2.5"/></svg>Builders Health Fund</div>
  </div>
  <div class="plan-row">
    <div class="plan"><svg class="tick" width="16" height="14" viewBox="0 0 16 14"><path d="M1 7 6 12 15 1" fill="none" stroke="#E54698" stroke-width="2.5"/></svg>Oakridge Medical Group</div>
    <div class="plan"><svg class="tick" width="16" height="14" viewBox="0 0 16 14"><path d="M1 7 6 12 15 1" fill="none" stroke="#E54698" stroke-width="2.5"/></svg>Shieldline Prime</div>
    <div class="plan"><svg class="tick" width="16" height="14" viewBox="0 0 16 14"><path d="M1 7 6 12 15 1" fill="none" stroke="#E54698" stroke-width="2.5"/></svg>Meadow Physicians</div>
    <div class="plan"><svg class="tick" width="16" height="14" viewBox="0 0 16 14"><path d="M1 7 6 12 15 1" fill="none" stroke="#E54698" stroke-width="2.5"/></svg>Everpoint Open Access</div>
    <div class="plan"><svg class="tick" width="16" height="14" viewBox="0 0 16 14"><path d="M1 7 6 12 15 1" fill="none" stroke="#E54698" stroke-width="2.5"/></svg>Crestline Select</div>
  </div>
  <div class="plan-row">
    <div class="plan"><svg class="tick" width="16" height="14" viewBox="0 0 16 14"><path d="M1 7 6 12 15 1" fill="none" stroke="#E54698" stroke-width="2.5"/></svg>Bluewater Plan</div>
    <div class="plan"><svg class="tick" width="16" height="14" viewBox="0 0 16 14"><path d="M1 7 6 12 15 1" fill="none" stroke="#E54698" stroke-width="2.5"/></svg>Northstar</div>
    <div class="plan"><svg class="tick" width="16" height="14" viewBox="0 0 16 14"><path d="M1 7 6 12 15 1" fill="none" stroke="#E54698" stroke-width="2.5"/></svg>Northstar Local Plus</div>
    <div class="plan"><svg class="tick" width="16" height="14" viewBox="0 0 16 14"><path d="M1 7 6 12 15 1" fill="none" stroke="#E54698" stroke-width="2.5"/></svg>Medara</div>
    <div class="plan"><svg class="tick" width="16" height="14" viewBox="0 0 16 14"><path d="M1 7 6 12 15 1" fill="none" stroke="#E54698" stroke-width="2.5"/></svg>Civicare</div>
    <div class="plan"><svg class="tick" width="16" height="14" viewBox="0 0 16 14"><path d="M1 7 6 12 15 1" fill="none" stroke="#E54698" stroke-width="2.5"/></svg>Wellnet</div>
    <div class="plan"><svg class="tick" width="16" height="14" viewBox="0 0 16 14"><path d="M1 7 6 12 15 1" fill="none" stroke="#E54698" stroke-width="2.5"/></svg>Harmona</div>
  </div>
  <div class="plan-row">
    <div class="plan"><svg class="tick" width="16" height="14" viewBox="0 0 16 14"><path d="M1 7 6 12 15 1" fill="none" stroke="#E54698" stroke-width="2.5"/></svg>Steelworks Trust Fund</div>
    <div class="plan"><svg class="tick" width="16" height="14" viewBox="0 0 16 14"><path d="M1 7 6 12 15 1" fill="none" stroke="#E54698" stroke-width="2.5"/></svg>Postal Carriers Plan</div>
    <div class="plan"><svg class="tick" width="16" height="14" viewBox="0 0 16 14"><path d="M1 7 6 12 15 1" fill="none" stroke="#E54698" stroke-width="2.5"/></svg>Engineers Health Plan</div>
    <div class="plan"><svg class="tick" width="16" height="14" viewBox="0 0 16 14"><path d="M1 7 6 12 15 1" fill="none" stroke="#E54698" stroke-width="2.5"/></svg>Metal Trades Plan</div>
    <div class="plan"><svg class="tick" width="16" height="14" viewBox="0 0 16 14"><path d="M1 7 6 12 15 1" fill="none" stroke="#E54698" stroke-width="2.5"/></svg>Shieldline Select</div>
  </div>
  <div class="plan-row last">
    <div class="plan"><svg class="tick" width="16" height="14" viewBox="0 0 16 14"><path d="M1 7 6 12 15 1" fill="none" stroke="#E54698" stroke-width="2.5"/></svg>Unity Health Plan</div>
    <div class="plan"><svg class="tick" width="16" height="14" viewBox="0 0 16 14"><path d="M1 7 6 12 15 1" fill="none" stroke="#E54698" stroke-width="2.5"/></svg>Grocers Union Plan</div>
    <div class="plan"><svg class="tick" width="16" height="14" viewBox="0 0 16 14"><path d="M1 7 6 12 15 1" fill="none" stroke="#E54698" stroke-width="2.5"/></svg>Meridian Benefits</div>
    <div class="plan"><svg class="tick" width="16" height="14" viewBox="0 0 16 14"><path d="M1 7 6 12 15 1" fill="none" stroke="#E54698" stroke-width="2.5"/></svg>Primeway of Sunridge</div>
  </div>
</div>

<!-- footer -->
<footer class="abs footer"></footer>
<div class="abs foot-logo"><i class="logo-dot"></i><span>Luma Women's Care</span></div>
<div class="abs foot-addr"><svg width="14" height="18" viewBox="0 0 12 16"><path d="M6 0a6 6 0 0 0-6 6c0 4.5 6 10 6 10s6-5.5 6-10a6 6 0 0 0-6-6zm0 8.5A2.5 2.5 0 1 1 6 3.5a2.5 2.5 0 0 1 0 5z" fill="#fff"/></svg>1840 Willow Crest Drive, Suite 120, Lakeview, CA 92500</div>
<div class="abs foot-contact">
  <svg width="16" height="14" viewBox="0 0 14 12"><path d="M0 5 14 0 10 12 7 7z" fill="#fff"/></svg>admin@lumawomenscare.com
  <span>|</span>
  <svg width="16" height="16" viewBox="0 0 24 24"><path d="M6.6 10.8a15 15 0 0 0 6.6 6.6l2.2-2.2c.3-.3.7-.4 1-.2 1.1.4 2.3.6 3.6.6.6 0 1 .4 1 1V20c0 .6-.4 1-1 1A17 17 0 0 1 3 4c0-.6.4-1 1-1h3.5c.6 0 1 .4 1 1 0 1.3.2 2.5.6 3.6.1.3 0 .7-.2 1z" fill="#fff"/></svg>555- 610- 2480
</div>
<nav class="abs foot-nav"><span>Home</span><span>About Us</span><span>Services</span><span>Resources</span><span>Contact</span></nav>
<div class="abs foot-copy">©2022 LUMA WOMEN'S CARE. ALL RIGHTS RESERVED<br>Terms &nbsp;|&nbsp; Privacy &nbsp;|&nbsp; Cookies</div>
<div class="abs foot-social"><i></i><i></i><i></i><i></i><i></i></div>

</body>
</html>
```